Graphic of Teacher Agility Framework

I need a model designed for my teacher educator agility framework. The concepts are responsive to each other on Figure 12 on the attachment and the text explains it all.

This is meant to be a conceptual framework of how ones thinks between experience, and theory, and research.

The domains represent a hierarchy of knowledge of specific domains that have enabled my learning to develop in-depth. I chose the term ‘agility framework’ to emphasise the importance of a responsiveness to the context and of the ability to respond with urgency between the various components (The Quillmark, 2012). I present the agility framework in Figure 12. The concentric circles are inter-connected as they are inter-dependent aspects of developing personal empowerment. The applicability of each domain relies on my ability to be aware of the context and to build work with urgency.

My learning has been iterative throughout this research, so this framework is intended to be understood as iterative, with movement between the concentric circles at a cognitive and behavioural level when greater awareness is gained. At the heart of the main circle are the researcherly dispositions that have been essential to my research and professional roles as well as to my personal learning. I have used descriptive headings for these dispositions that I believe are helpful for understanding them. The first one, ‘value deep understanding’, is modelled on Vostrup (2019); whilst ‘cognitive flexibility’ is an inter-cultural competency from Brasko et al (2014). I have also added in ‘responsiveness’ and ‘sensory awareness’ which I believe are additional dispositions that have emerged in this study. Whilst conducting this research I have been responsive to the context, the participants, and the data, whilst gaining a greater awareness of my place within UAE society.

Target Market(s)

Academic, research

Requirements
Must have
• Attractive Visuals
Nice to have
• Connections between the concepts

```html
<!DOCTYPE html>
<html lang="en">
<head>
<meta charset="utf-8">
<title>Teacher Educator Agility Framework</title>
<link href="https://fonts.googleapis.com/css2?family=Arimo:wght@400;700&display=swap" rel="stylesheet">
<style>
  :root {
    --blue: #0071bc;
    --amber: #f7b21c;
    --amber-box: #fdbb0f;
    --green: #6a9a23;
    --purple: #8a56a0;
    --red: #e04a4a;
    --venn-yellow: #fdc02a;
    --venn-red: #e0474f;
    --venn-blue: #1c7cc0;
    --venn-purple: #8d58a6;
    --ink: #111111;
    --paper: #ffffff;
  }
  html, body {
    margin: 0;
    padding: 0;
    width: 1174px;
    height: 1200px;
    overflow: hidden;
    background: var(--paper);
  }
  .framework {
    display: block;
    width: 1174px;
    height: 1200px;
    font-family: "Arimo", Arial, sans-serif;
    font-weight: 700;
  }
  .ring-blue { fill: none; stroke: var(--blue); stroke-width: 55; }
  .arc-context { fill: none; stroke: var(--amber); stroke-width: 55; }
  .arc-relationships { fill: none; stroke: var(--green); stroke-width: 55; }
  .head-context { fill: var(--amber); }
  .head-relationships { fill: var(--green); stroke: var(--paper); stroke-width: 3; }
  .research-disc { fill: var(--purple); }
  .disposition-disc { fill: var(--red); stroke: var(--paper); stroke-width: 12; }
  .quadrant-line { stroke: var(--paper); stroke-width: 2; }
  .label-light { fill: var(--paper); }
  .label-dark { fill: var(--ink); }
  .timeline { fill: none; stroke: var(--blue); stroke-width: 1.5; }
  .timeline-dot { fill: var(--blue); }
  .factor-box { fill: var(--amber-box); }
  .tick-ring { fill: none; stroke: var(--paper); stroke-width: 1.2; }
  .tick-mark { fill: none; stroke: var(--paper); stroke-width: 1.4; }
  .link-context { fill: var(--amber); stroke: var(--paper); stroke-width: 2.5; }
  .link-relationships { fill: var(--green); stroke: var(--paper); stroke-width: 2.5; }
  .venn { opacity: 0.8; }
  .empower-arrow { fill: none; stroke: var(--green); stroke-width: 1.6; }
</style>
</head>
<body>
<svg class="framework" viewBox="0 0 1080 1104" preserveAspectRatio="xMinYMin meet" xmlns="http://www.w3.org/2000/svg" role="img" aria-label="Teacher educator agility framework">
  <defs>
    <path id="path-intercultural" d="M 306 367 A 274 274 0 0 0 854 367"/>
    <path id="path-research" d="M 452 367 A 128 128 0 0 1 708 367"/>
  </defs>

  <g class="awareness-timeline">
    <path class="timeline" d="M 581 57 A 310 310 0 0 1 581 677"/>
    <circle class="timeline-dot" cx="581" cy="57" r="5.5"/>
    <circle class="timeline-dot" cx="581" cy="677" r="5.5"/>
    <circle class="timeline-dot" cx="874" cy="269" r="5.5"/>
    <circle class="timeline-dot" cx="886" cy="318" r="5.5"/>
    <circle class="timeline-dot" cx="890" cy="367" r="5.5"/>
    <circle class="timeline-dot" cx="886" cy="416" r="5.5"/>
    <circle class="timeline-dot" cx="874" cy="465" r="5.5"/>
    <g class="label-dark" font-size="11">
      <text x="900" y="273">Time</text>
      <text x="910" y="322">Speed</text>
      <text x="915" y="371">Urgency</text>
      <text x="904" y="421">Awareness of self</text>
      <text x="896" y="469">Reflexivity</text>
    </g>
  </g>

  <circle class="ring-blue" cx="580" cy="367" r="266"/>
  <text class="label-light" font-size="14">
    <textPath href="#path-intercultural" startOffset="50%" text-anchor="middle">Inter-cultural competence</textPath>
  </text>

  <path class="arc-context" d="M 384 332 A 202 202 0 0 1 782 367"/>
  <polygon class="head-context" points="734,367 826,367 780,411"/>
  <text class="label-light" x="584" y="177" font-size="15" text-anchor="middle">Context</text>

  <path class="arc-relationships" d="M 780 395 A 202 202 0 0 1 380 367"/>
  <polygon class="head-relationships" points="340,368 424,368 382,323"/>
  <text class="label-light" x="580" y="566" font-size="15" text-anchor="middle">Relationships</text>

  <circle class="research-disc" cx="580" cy="367" r="163"/>
  <text class="label-light" font-size="14">
    <textPath href="#path-research" startOffset="50%" text-anchor="middle">Consumption of Research</textPath>
  </text>

  <circle class="disposition-disc" cx="580" cy="367" r="110"/>
  <line class="quadrant-line" x1="580" y1="263" x2="580" y2="471"/>
  <line class="quadrant-line" x1="476" y1="367" x2="684" y2="367"/>
  <g class="label-light" font-size="11" text-anchor="middle">
    <text x="540" y="323">Sensory</text>
    <text x="533" y="337">Awareness</text>
    <text x="621" y="325">Value Deep</text>
    <text x="631" y="339">Understanding</text>
    <text x="533" y="411" font-size="10">Responsiveness</text>
    <text x="618" y="411">Cognitive</text>
    <text x="618" y="425">Flexibility</text>
  </g>

  <rect class="factor-box" x="70" y="108" width="198" height="145" rx="18"/>
  <g class="factor-list label-light" font-size="11">
    <g transform="translate(95 156)"><circle class="tick-ring" r="5.5"/><path class="tick-mark" d="M -2.5 0 L -0.5 2.5 L 4 -4"/></g>
    <text x="113" y="160">Employment Contracts</text>
    <g transform="translate(95 174)"><circle class="tick-ring" r="5.5"/><path class="tick-mark" d="M -2.5 0 L -0.5 2.5 L 4 -4"/></g>
    <text x="113" y="179">Cultural Differences</text>
    <g transform="translate(95 193)"><circle class="tick-ring" r="5.5"/><path class="tick-mark" d="M -2.5 0 L -0.5 2.5 L 4 -4"/></g>
    <text x="113" y="197">Education Regulations</text>
    <g transform="translate(95 212)"><circle class="tick-ring" r="5.5"/><path class="tick-mark" d="M -2.5 0 L -0.5 2.5 L 4 -4"/></g>
    <text x="113" y="217">Macro Economic Factors</text>
  </g>

  <polygon class="link-context" points="283,216 308,191 308,206 442,206 442,191 470,216 442,241 442,226 308,226 308,241"/>
  <polygon class="link-relationships" points="283,527 308,502 308,517 442,517 442,502 470,527 442,552 442,537 308,537 308,552"/>

  <g class="label-dark" font-size="11" text-anchor="middle">
    <text x="172" y="328">Personal</text>
    <text x="172" y="343">Empowerment</text>
  </g>
  <path class="empower-arrow" d="M 172 432 L 172 361 M 160 373 L 172 361 L 184 373"/>

  <g class="empowerment-venn">
    <circle class="venn" cx="135" cy="492" r="60" fill="var(--venn-yellow)"/>
    <circle class="venn" cx="208" cy="492" r="60" fill="var(--venn-red)"/>
    <circle class="venn" cx="135" cy="569" r="60" fill="var(--venn-blue)"/>
    <circle class="venn" cx="208" cy="569" r="60" fill="var(--venn-purple)"/>
  </g>
  <g class="label-light" font-size="11" text-anchor="middle">
    <text x="118" y="495">Agency</text>
    <text x="227" y="495">Tensions</text>
    <text x="131" y="569">Tacit</text>
    <text x="113" y="583">Knowledge</text>
    <text x="220" y="572">Power</text>
    <text x="220" y="586">Grow</text>
  </g>
</svg>
</body>
</html>
```